Web Design Project - Pinecrest & Tours

Live long and prosper!
The page aims people willing to book holidays and health prevention courses in combination. The ZUR-Method is a concept of defined:
* EXERCISES: walking, fitness, yoga, ...
* RELAXATION: massage, spa, ...
* NUTRITION: diets (more, less, selected)
Doing in a group brings fun and social community.
When wanted a doctor or health professional supports the stay.
The page explains all courses, all benefits and all locations to stay.
Health

```html
<!DOCTYPE html>
<html lang="en">
<head>
<meta charset="utf-8">
<title>Contact Us – Pinecrest &amp; Tours</title>
<link href="https://fonts.googleapis.com/css2?family=Arimo:wght@400;700&family=PT+Sans:wght@400;700&family=Tinos:wght@700&display=swap" rel="stylesheet">
<style>
:root{
  --page-bg:#d9d9d9;
  --panel:#ffffff;
  --nav-bg:#f7f7f7;
  --footer-bg:#ececec;
  --brand-green:#8cbf26;
  --accent-green:#b4d93a;
  --accent-green-dark:#93b92a;
  --ink:#2b2b2b;
  --ink-soft:#555555;
  --ink-muted:#8a8a8a;
  --line:#cfcfcf;
  --select-blue:#5a9de8;
}
*{box-sizing:border-box;margin:0;padding:0}
html,body{width:1200px;height:1101px;overflow:hidden}
body{background:var(--page-bg);font-family:"Arimo",Arial,sans-serif;color:var(--ink);position:relative}
.brand{position:absolute;left:87px;top:88px;font-family:"PT Sans",sans-serif;font-weight:700;font-size:29px;color:var(--brand-green);letter-spacing:.5px;text-transform:uppercase}
.page{position:absolute;left:52px;top:140px;width:1108px;height:898px;background:var(--panel);border-radius:3px;overflow:hidden}
.main-nav{height:66px;background:var(--nav-bg);display:flex;align-items:center;padding-left:50px}
.main-nav a{font-family:"Tinos",serif;font-weight:700;font-size:13px;color:#333;text-decoration:none;margin-right:28px}
.main-nav a.current{background:var(--accent-green);color:#fff;padding:11px 10px;border-radius:4px;border:2px solid #d6ec8f;box-shadow:0 0 0 1px var(--accent-green-dark);margin-left:-10px}
.title-band{position:absolute;left:40px;top:70px;width:1016px;height:85px;background:linear-gradient(90deg,rgba(242,238,240,0),#f1edef 12%,#f1edef 88%,rgba(242,238,240,0));border-bottom:1px solid #e2e2e2}
.title-band h1{font-family:"PT Sans",sans-serif;font-size:29px;font-weight:700;text-align:center;line-height:85px;color:#2a2a2a}
.intro{position:absolute;left:44px;top:196px;width:650px;font-size:15px;line-height:22px;color:var(--ink-soft)}
.field-label{position:absolute;font-family:"PT Sans",sans-serif;font-size:15px;color:#222}
.field{position:absolute;background:#fff;border:2px solid #bdbdbd;border-radius:5px;box-shadow:inset 0 2px 5px rgba(0,0,0,.35)}
.select-arrow{position:absolute;right:-1px;top:-1px;width:30px;height:36px;background:var(--select-blue);border-radius:4px;display:flex;align-items:center;justify-content:center}
.message{position:absolute;left:44px;top:493px;width:599px;height:196px;border:1px solid var(--line);border-radius:4px}
.send-btn{position:absolute;left:42px;top:717px;width:126px;height:31px;border:1px solid #c8c8c8;border-radius:4px;background:linear-gradient(#fafafa,#ececec);font-family:"PT Sans",sans-serif;font-size:13px;color:#222;display:flex;align-items:center;justify-content:center}
.contact-card{position:absolute;left:704px;top:197px;width:353px;height:261px;border:1px solid var(--line)}
.contact-card h2{height:48px;border-bottom:1px solid var(--line);font-family:"PT Sans",sans-serif;font-size:15px;font-weight:400;text-align:center;line-height:47px;color:#222}
.contact-item{display:flex;align-items:center;height:69px;margin:0 16px;border-bottom:1px solid #ececec}
.contact-item:last-child{border-bottom:none}
.contact-item svg{flex:none;margin-right:18px}
.contact-item strong{display:block;font-family:"PT Sans",sans-serif;font-weight:400;font-size:14px;color:#333}
.contact-item span{display:block;font-size:13px;color:var(--ink-muted)}
.site-footer{position:absolute;left:0;top:797px;width:1108px;height:101px;background:var(--footer-bg)}
.copyright{position:absolute;left:46px;top:42px;font-family:"PT Sans",sans-serif;font-weight:700;font-size:16px;color:#6a6a6a}
.social{position:absolute;right:52px;top:38px;display:flex;gap:8px}
.social span{width:25px;height:25px;background:#d2d2d2;border:1px solid #bdbdbd;border-radius:3px}
</style>
</head>
<body>
<div class="brand">Pinecrest &amp; Tours</div>
<div class="page">
  <nav class="main-nav">
    <a href="#">Home</a><a href="#">Our Services</a><a href="#">Why Us?</a><a href="#">Exercises</a><a href="#">Relaxation</a><a href="#">Nutritions</a><a href="#" class="current">Contact Us</a>
  </nav>
  <div class="title-band"><h1>Contact Us</h1></div>
  <p class="intro">Sed congue eleifend ultrices. Curabitur aliquet ipsum sit nim condimentum quis. Curabitur id mauris felis. t gravida nibh. Nunc scelerisque odio elementum</p>

  <label class="field-label" style="left:44px;top:268px">Your Name</label>
  <div class="field" style="left:44px;top:299px;width:292px;height:36px"></div>
  <label class="field-label" style="left:348px;top:268px">Your Email</label>
  <div class="field" style="left:348px;top:299px;width:292px;height:36px"></div>

  <label class="field-label" style="left:44px;top:365px">Your Phone Number</label>
  <div class="field" style="left:44px;top:395px;width:292px;height:38px"></div>
  <label class="field-label" style="left:350px;top:365px">Subject</label>
  <div class="field" style="left:348px;top:395px;width:292px;height:38px">
    <div class="select-arrow"><svg width="10" height="7" viewBox="0 0 10 7"><path d="M1 1l4 4 4-4" fill="none" stroke="#1d2f4a" stroke-width="2"/></svg></div>
  </div>

  <label class="field-label" style="left:44px;top:462px">Message / Question</label>
  <div class="message"></div>
  <div class="send-btn">Send Message</div>

  <aside class="contact-card">
    <h2>Pinecrest &amp; Tours Headquarters</h2>
    <div class="contact-item">
      <svg width="30" height="30" viewBox="0 0 30 30"><circle cx="15" cy="15" r="15" fill="var(--accent-green)"/><rect x="8" y="10" width="14" height="10" rx="1" fill="#fff"/><path d="M8 10l7 6 7-6" fill="none" stroke="var(--accent-green)" stroke-width="1.5"/></svg>
      <div><strong>By E-mail</strong><span>hello@pinecresttours.example</span></div>
    </div>
    <div class="contact-item">
      <svg width="30" height="30" viewBox="0 0 30 30"><circle cx="15" cy="15" r="15" fill="var(--accent-green)"/><path d="M7 13c0-3 16-3 16 0v2h-4v-2h-8v2H7z" fill="#fff"/><rect x="10" y="16" width="10" height="6" rx="1" fill="#fff"/></svg>
      <div><strong>By Phone</strong><span>1-555-204-7731</span></div>
    </div>
    <div class="contact-item">
      <svg width="30" height="30" viewBox="0 0 30 30"><circle cx="15" cy="15" r="15" fill="var(--accent-green)"/><rect x="8" y="12" width="14" height="10" rx="1" fill="#fff"/><rect x="11" y="8" width="8" height="5" fill="#fff"/></svg>
      <div><strong>By Fax</strong><span>1-555-204-7732</span></div>
    </div>
  </aside>

  <footer class="site-footer">
    <p class="copyright">Copyright 2011. All Rights Reserved.</p>
    <div class="social"><span></span><span></span><span></span></div>
  </footer>
</div>
</body>
</html>
```